Refresh of graphic design for existing website

We would like to refresh our website. Please see the attached design specifications.

Industry/Entity Type

Graphic Design

```html
<!DOCTYPE html>
<html lang="en">
<head>
<meta charset="utf-8">
<title>The Service and Tool Alliance</title>
<link href="https://fonts.googleapis.com/css2?family=Open+Sans:wght@400;600;700&display=swap" rel="stylesheet">
<style>
:root{
  --green:#1e8e3e;
  --green-dark:#12652a;
  --nav:#0f5a2a;
  --blue:#1c63b3;
  --blue-deep:#134a8c;
  --navy:#0c2747;
  --ink:#333;
  --muted:#777;
  --line:#d6d6d6;
  --white:#fff;
}
*{box-sizing:border-box;margin:0;padding:0}
html,body{width:747px;height:1200px;overflow:hidden}
body{font-family:"Open Sans",Arial,sans-serif;color:var(--ink);background:var(--white);font-size:9px}
.site-header{height:85px;display:flex;align-items:center;padding:0 28px;position:relative}
.brand{display:flex;align-items:center;gap:8px}
.brand-mark{width:16px;height:16px;border-radius:50%;background:var(--green)}
.brand-name{font-weight:700;font-size:26px;color:var(--green);letter-spacing:1px}
.brand-title{margin-left:28px;font-size:13px;color:#444}
.social{display:flex;gap:8px;margin-left:18px}
.social span{width:11px;height:11px;border-radius:50%;background:#555}
.login{position:absolute;right:18px;top:8px;width:150px;font-size:8px;color:#666}
.login-row{display:flex;align-items:center;justify-content:space-between;margin-bottom:5px}
.login-row input{width:95px;height:14px;border:1px solid var(--line)}
.login-actions{display:flex;align-items:center;gap:6px}
.btn-login{background:var(--green);color:#fff;font-weight:700;font-size:8px;padding:3px 10px;border:0}
.login-extra{line-height:1.3}
.main-nav{height:35px;background:var(--nav);display:flex;align-items:center;padding:0 16px}
.main-nav a{color:#fff;text-decoration:none;font-size:8px;font-weight:600;padding:0 10px;height:35px;line-height:35px}
.main-nav a.active{background:var(--green)}
.search{margin-left:auto;display:flex}
.search input{width:110px;height:17px;border:0}
.search button{width:18px;height:17px;border:0;background:var(--green)}
.hero{height:355px;position:relative;background:linear-gradient(90deg,#2a3342 0%,#3c4a5c 40%,#4d5a66 65%,#2c3540 100%)}
.hero-copy{position:absolute;left:440px;top:105px;color:#fff}
.hero-copy h1{font-weight:400;font-size:30px;line-height:1.15}
.hero-copy p{font-size:15px;margin-top:10px;line-height:1.3}
.intro{text-align:center;padding:38px 40px 0}
.intro h2{color:var(--green);font-size:21px;font-weight:600}
.intro hr{width:180px;border:0;border-top:2px solid var(--green);margin:8px auto 16px}
.intro p{font-size:8.5px;color:#555;line-height:1.55;margin-bottom:8px}
.columns{display:flex;gap:20px;padding:20px 40px 0}
.panel{flex:1;border:1px solid var(--line);height:250px}
.panel h3{background:var(--green);color:#fff;font-size:17px;font-weight:600;padding:6px 12px}
.panel-body{padding:10px 12px;line-height:1.5}
.item{margin-bottom:14px}
.item h4{font-size:10px;font-weight:700;color:#222}
.meta{color:var(--muted);font-size:7.5px}
.more{color:var(--green);font-size:8px;font-weight:600}
.event h4{font-size:9.5px;font-weight:700}
.event{border-bottom:1px solid var(--line);padding-bottom:8px;margin-bottom:9px}
.quick{margin-top:35px;height:215px;background:linear-gradient(180deg,var(--blue) 0%,var(--blue-deep) 100%);color:#fff;padding:22px 60px}
.quick h3{text-align:center;font-size:20px;font-weight:600;letter-spacing:1px}
.quick hr{width:120px;border:0;border-top:2px solid #fff;margin:6px auto 18px}
.quick-grid{display:flex;justify-content:space-between}
.quick-grid ul{list-style:none}
.quick-grid li{font-size:8.5px;margin-bottom:9px;display:flex;align-items:center;gap:6px}
.quick-grid svg{width:7px;height:7px}
.site-footer{height:60px;background:var(--navy);color:#c7d2e0;text-align:center;font-size:8px;padding-top:16px;line-height:1.7}
</style>
</head>
<body>
<header class="site-header">
  <div class="brand"><span class="brand-mark"></span><span class="brand-name">STA</span></div>
  <div class="brand-title">The Service and Tool Alliance</div>
  <div class="social"><span></span><span></span><span></span></div>
  <form class="login">
    <div class="login-row"><label>Email</label><input type="text"></div>
    <div class="login-row"><label>Password</label><input type="password"></div>
    <div class="login-actions"><button class="btn-login" type="button">LOGIN</button><div class="login-extra">☐ Remember Me<br>Forgot Password?</div></div>
  </form>
</header>
<nav class="main-nav">
  <a class="active">HOME</a><a>ABOUT STA</a><a>MEMBERSHIP</a><a>STA MEMBERS</a><a>TECHBASE LIBRARY</a><a>MARKET RESEARCH</a><a>INDUSTRY FAQS</a><a>CONTACT US</a>
  <div class="search"><input type="text" placeholder=" Search"><button type="button"></button></div>
</nav>
<section class="hero">
  <div role="img" aria-label="Technician in a work shirt holding a diagnostic tool in a repair garage" style="position:absolute;inset:0"></div>
  <div class="hero-copy">
    <h1>The Service<br>&amp; Tool Alliance</h1>
    <p>Serving the automotive repair<br>industry since 1947.</p>
  </div>
</section>
<section class="intro">
  <h2>Serving the automotive repair industry since 1947.</h2>
  <hr>
  <p>STA's Mission is to advance the vehicle service industry by providing technical data and open dialog between the manufacturers of transportation products, government regulators and the providers of tools, equipment and service information.</p>
  <p>STA is one of the most respected trade associations in the automotive aftermarket, giving fair and equitable representation to all segments of the equipment and tool industry. The Alliance is an association of automotive tool and equipment manufacturers and technical information providers and training organizations.</p>
</section>
<section class="columns">
  <article class="panel">
    <h3>Breaking News</h3>
    <div class="panel-body">
      <div class="item">
        <h4>Hacking: It's Everybody's Concern</h4>
        <div class="meta">Tue, 24 Sep 2013 09:30:00 GMT</div>
        <p class="meta">Contributed by Dan Porter, Senior Partner, Roadline Media LLC Remote hacking is a threat the automotive industry</p>
        <div class="more">Continue reading »</div>
      </div>
      <div class="item">
        <h4>Telecoms Bridge the Connectivity Gap</h4>
        <div class="meta">Mon, 16 Sep 2013 08:00:00 GMT</div>
        <p class="meta">Contributed by Dan Porter, Senior Partner, Roadline Media LLC The annual conference — one of three annual automotive conferences</p>
        <div class="more">Continue reading »</div>
      </div>
    </div>
  </article>
  <article class="panel">
    <h3>Industry Events</h3>
    <div class="panel-body">
      <div class="event"><h4>AutoParts Expo</h4><div class="meta">Nov 4, 2014</div><div class="meta">Desert Expo Hall, Las Vegas, Nevada</div></div>
      <div class="event"><h4>Custom Motor Show</h4><div class="meta">Nov 4, 2014</div><div class="meta">Silver Convention Hall, Las Vegas NV</div></div>
      <div class="event"><h4>Winter Tech Week 2015</h4><div class="meta">Jan 26, 2015</div><div class="meta">Harbor Point, CA</div></div>
    </div>
  </article>
</section>
<section class="quick">
  <h3>QUICK LINKS</h3>
  <hr>
  <div class="quick-grid">
    <ul>
      <li><svg viewBox="0 0 8 8"><path d="M2 1l4 3-4 3z" fill="#fff"/></svg>TechBase Library</li>
      <li><svg viewBox="0 0 8 8"><path d="M2 1l4 3-4 3z" fill="#fff"/></svg>STA News Blog</li>
      <li><svg viewBox="0 0 8 8"><path d="M2 1l4 3-4 3z" fill="#fff"/></svg>STA Member Companies</li>
      <li><svg viewBox="0 0 8 8"><path d="M2 1l4 3-4 3z" fill="#fff"/></svg>STA Active Participants</li>
      <li><svg viewBox="0 0 8 8"><path d="M2 1l4 3-4 3z" fill="#fff"/></svg>Investment Planning Guide</li>
    </ul>
    <ul>
      <li><svg viewBox="0 0 8 8"><path d="M2 1l4 3-4 3z" fill="#fff"/></svg>STA Market Research Surveys</li>
      <li><svg viewBox="0 0 8 8"><path d="M2 1l4 3-4 3z" fill="#fff"/></svg>Payment Center</li>
      <li><svg viewBox="0 0 8 8"><path d="M2 1l4 3-4 3z" fill="#fff"/></svg>State-by-State Emissions</li>
      <li><svg viewBox="0 0 8 8"><path d="M2 1l4 3-4 3z" fill="#fff"/></svg>Tool Program Update</li>
      <li><svg viewBox="0 0 8 8"><path d="M2 1l4 3-4 3z" fill="#fff"/></svg>Data Flowchart</li>
    </ul>
    <ul>
      <li><svg viewBox="0 0 8 8"><path d="M2 1l4 3-4 3z" fill="#fff"/></svg>Issue Log</li>
      <li><svg viewBox="0 0 8 8"><path d="M2 1l4 3-4 3z" fill="#fff"/></svg>Collect Definitions</li>
      <li><svg viewBox="0 0 8 8"><path d="M2 1l4 3-4 3z" fill="#fff"/></svg>Writers and Presenters</li>
      <li><svg viewBox="0 0 8 8"><path d="M2 1l4 3-4 3z" fill="#fff"/></svg>Guidelines</li>
      <li><svg viewBox="0 0 8 8"><path d="M2 1l4 3-4 3z" fill="#fff"/></svg>OpenData Forum</li>
    </ul>
  </div>
</section>
<footer class="site-footer">
  Copyright © 2009-2015 Service and Tool Alliance<br>
  4120 Lakeview Drive, Suite 310, Millbrook, MI 48000 · 555-014-2080
</footer>
</body>
</html>
```